Criação de Papelaria (6 itens) para Arquitetura
" Sou recém formada em Design de Interiores e pretendo começar a divulgar meu negócio. Já fiz alguns trabalhos / projetos, mas ainda não consegui alavancar minha marca. Meu foco será a realização de projetos residenciais, comerciais e empresariais. As atividades vão desde a entrevista inicial para entendimento das necessidades do cliente, passando pela preparação dos projetos com imagens renderizadas, plantas baixas, projetos de marcenaria, iluminação, gesso etc., incluindo também acompanhamento a lojas para escolha de materiais / móveis até o acompanhamento da obra e fiscalização dos trabalhos executados por terceiros. "

```html
<!DOCTYPE html>
<html lang="pt-BR">
<head>
<meta charset="utf-8">
<title>Lia Moraes — Pasta</title>
<link rel="stylesheet" href="https://fonts.googleapis.com/css2?family=Montserrat:wght@300;400&display=swap">
<style>
  :root {
    --page-bg: #e4e2e6;
    --folder-top: #454050;
    --folder-bottom: #2f2b37;
    --fold-shade: rgba(0, 0, 0, 0.28);
    --rose: #d9a08e;
    --rose-deep: #b9796a;
    --rose-light: #f0c6b6;
    --text-light: #ece7ee;
    --text-muted: #a49dab;
    --ghost: rgba(255, 255, 255, 0.045);
  }
  * { box-sizing: border-box; margin: 0; padding: 0; }
  html, body { width: 1200px; height: 1200px; overflow: hidden; }
  body {
    background: var(--page-bg);
    font-family: "Montserrat", sans-serif;
    color: var(--text-light);
  }
  .folder-spread {
    position: absolute;
    left: 100px; top: 246px;
    width: 1000px; height: 708px;
    display: flex;
    box-shadow: 0 20px 50px rgba(0, 0, 0, 0.25);
  }
  .folder-panel {
    position: relative;
    width: 500px; height: 708px;
    background: linear-gradient(160deg, var(--folder-top), var(--folder-bottom));
    overflow: hidden;
  }
  .folder-panel--back::after {
    content: "";
    position: absolute; top: 0; right: 0;
    width: 40px; height: 100%;
    background: linear-gradient(90deg, transparent, var(--fold-shade));
  }
  .folder-panel--front::before {
    content: "";
    position: absolute; top: 0; left: 0;
    width: 30px; height: 100%;
    background: linear-gradient(90deg, var(--fold-shade), transparent);
  }
  .rose-line {
    position: absolute;
    height: 4px;
    background: linear-gradient(90deg, var(--rose-deep), var(--rose-light), var(--rose));
  }
  .rose-line--front { left: 0; right: 40px; top: 582px; }
  .rose-line--back { left: 240px; right: 0; top: 582px; }
  .edge-strip {
    position: absolute;
    right: 0; top: 110px;
    width: 5px; height: 180px;
    background: linear-gradient(180deg, var(--rose-light), var(--rose-deep));
  }
  .ghost-square {
    position: absolute;
    left: 30px; top: 110px;
    width: 260px; height: 260px;
    border: 34px solid var(--ghost);
  }
  .brand {
    position: absolute;
    text-align: center;
  }
  .brand--front { left: 110px; width: 340px; top: 250px; }
  .brand--back { left: 250px; width: 220px; top: 470px; }
  .brand-mark {
    display: block;
    margin: 0 auto;
    border: 2px solid var(--rose);
  }
  .brand--front .brand-mark { width: 34px; height: 34px; margin-bottom: 14px; }
  .brand--back .brand-mark { width: 20px; height: 20px; margin-bottom: 8px; }
  .brand-name {
    font-weight: 300;
    letter-spacing: 0.16em;
    text-transform: uppercase;
    color: var(--text-light);
    white-space: nowrap;
  }
  .brand--front .brand-name { font-size: 34px; }
  .brand--back .brand-name { font-size: 20px; }
  .brand-tagline {
    font-weight: 400;
    letter-spacing: 0.3em;
    text-transform: uppercase;
    color: var(--rose);
    white-space: nowrap;
  }
  .brand--front .brand-tagline { font-size: 9.5px; margin-top: 6px; }
  .brand--back .brand-tagline { font-size: 6px; margin-top: 4px; }
  .contact-list {
    position: absolute;
    left: 34px; top: 520px;
    list-style: none;
  }
  .contact-item {
    display: flex; align-items: center; gap: 10px;
    margin-bottom: 9px;
    font-size: 9px;
    line-height: 1.35;
    color: var(--text-muted);
    white-space: nowrap;
  }
  .contact-icon { width: 16px; height: 16px; flex: none; }
</style>
</head>
<body>
  <main class="folder-spread">
    <section class="folder-panel folder-panel--back" aria-label="Verso da pasta">
      <ul class="contact-list">
        <li class="contact-item">
          <svg class="contact-icon" viewBox="0 0 16 16" aria-hidden="true"><circle cx="8" cy="8" r="8" fill="var(--rose)"/><path d="M5.5 4.5l1.4 0 .6 1.8-.9.7a5 5 0 0 0 2.4 2.4l.7-.9 1.8.6v1.4c0 .4-.4.8-.9.7A6.5 6.5 0 0 1 4.8 5.4c-.1-.5.3-.9.7-.9z" fill="var(--folder-bottom)"/></svg>
          <span>+55 11 4000-1020<br>+55 11 98000-2030</span>
        </li>
        <li class="contact-item">
          <svg class="contact-icon" viewBox="0 0 16 16" aria-hidden="true"><circle cx="8" cy="8" r="8" fill="var(--rose)"/><rect x="4" y="5" width="8" height="6" fill="none" stroke="var(--folder-bottom)" stroke-width="1"/><path d="M4 5l4 3.2L12 5" fill="none" stroke="var(--folder-bottom)" stroke-width="1"/></svg>
          <span>contato@liamoraes.com</span>
        </li>
        <li class="contact-item">
          <svg class="contact-icon" viewBox="0 0 16 16" aria-hidden="true"><circle cx="8" cy="8" r="8" fill="var(--rose)"/><circle cx="8" cy="8" r="4" fill="none" stroke="var(--folder-bottom)" stroke-width="1"/><path d="M4 8h8M8 4c-2 2.4-2 5.6 0 8M8 4c2 2.4 2 5.6 0 8" fill="none" stroke="var(--folder-bottom)" stroke-width="0.8"/></svg>
          <span>www.liamoraes.com</span>
        </li>
        <li class="contact-item">
          <svg class="contact-icon" viewBox="0 0 16 16" aria-hidden="true"><circle cx="8" cy="8" r="8" fill="var(--rose)"/><path d="M8 12.5s-3.2-3.4-3.2-5.6a3.2 3.2 0 0 1 6.4 0C11.2 9.1 8 12.5 8 12.5z" fill="var(--folder-bottom)"/><circle cx="8" cy="6.9" r="1.1" fill="var(--rose)"/></svg>
          <span>Rua das Acácias, 210, Centro<br>CEP 01000-000, São Paulo</span>
        </li>
      </ul>
      <div class="brand brand--back">
        <span class="brand-mark"></span>
        <div class="brand-name">Lia Moraes</div>
        <div class="brand-tagline">Design de Interiores</div>
      </div>
      <div class="rose-line rose-line--back"></div>
    </section>

    <section class="folder-panel folder-panel--front" aria-label="Capa da pasta">
      <div class="ghost-square" aria-hidden="true"></div>
      <div class="brand brand--front">
        <span class="brand-mark"></span>
        <div class="brand-name">Lia Moraes</div>
        <div class="brand-tagline">Design de Interiores</div>
      </div>
      <div class="edge-strip"></div>
      <div class="rose-line rose-line--front"></div>
    </section>
  </main>
</body>
</html>
```